5Marble Strategy- Logo & Design Work

THIS IS PHASE ONE. I have a stock trading strategy. I need a schematic that shows how it works. I have included sketches. I want the scheme to look like Exhibit A. I want the circles to look like gear shifts in Exhibit B. After this first step is done, we will move on to creating logo like Exhibit C, a second logo like Exhibit D and another Schematic like Exhibit E.

```html
<!DOCTYPE html>
<html lang="en">
<head>
<meta charset="utf-8">
<title>5Marble Strategy – Schematic</title>
<link href="https://fonts.googleapis.com/css2?family=Open+Sans:wght@700&display=swap" rel="stylesheet">
<style>
  :root {
    --bg: #ffffff;
    --ring-green: #1a8a3e;
    --gear-dark: #1a8a3e;
    --gear-light: #43a548;
    --label: #ffffff;
    --arrow-edge: #1f5fab;
    --arrow-core: #2aa6d2;
  }
  html, body {
    margin: 0;
    padding: 0;
    width: 1200px;
    height: 927px;
    overflow: hidden;
    background: var(--bg);
  }
  .schematic {
    display: block;
    width: 1200px;
    height: 927px;
  }
  .orbit-ring {
    fill: none;
    stroke: var(--ring-green);
    stroke-width: 22;
  }
  .gear-gap { fill: var(--bg); stroke: var(--bg); stroke-width: 10; }
  .gear-face { fill: url(#gearShade); }
  .gear-hub { fill: var(--gear-dark); stroke: var(--label); stroke-width: 1.6; }
  .gear-label {
    font-family: "Open Sans", sans-serif;
    font-weight: 700;
    font-size: 17px;
    fill: var(--label);
    text-anchor: middle;
  }
  .gear-note {
    font-family: "Open Sans", sans-serif;
    font-weight: 700;
    font-size: 8.5px;
    fill: var(--label);
    text-anchor: middle;
  }
  .flow-arrow { fill: url(#arrowShade); }
</style>
</head>
<body>
<svg class="schematic" viewBox="0 0 1200 927" xmlns="http://www.w3.org/2000/svg">
  <defs>
    <radialGradient id="gearShade" gradientUnits="userSpaceOnUse" cx="0" cy="0" r="99">
      <stop offset="0.65" stop-color="var(--gear-dark)"/>
      <stop offset="1" stop-color="var(--gear-light)"/>
    </radialGradient>
    <linearGradient id="arrowShade" x1="0" y1="0" x2="0" y2="1">
      <stop offset="0" stop-color="var(--arrow-edge)"/>
      <stop offset="0.5" stop-color="var(--arrow-core)"/>
      <stop offset="1" stop-color="var(--arrow-edge)"/>
    </linearGradient>

    <g id="gearTeeth">
      <circle r="86"/>
      <rect x="-14" y="-99" width="28" height="30" rx="2"/>
      <rect x="-14" y="-99" width="28" height="30" rx="2" transform="rotate(30)"/>
      <rect x="-14" y="-99" width="28" height="30" rx="2" transform="rotate(60)"/>
      <rect x="-14" y="-99" width="28" height="30" rx="2" transform="rotate(90)"/>
      <rect x="-14" y="-99" width="28" height="30" rx="2" transform="rotate(120)"/>
      <rect x="-14" y="-99" width="28" height="30" rx="2" transform="rotate(150)"/>
      <rect x="-14" y="-99" width="28" height="30" rx="2" transform="rotate(180)"/>
      <rect x="-14" y="-99" width="28" height="30" rx="2" transform="rotate(210)"/>
      <rect x="-14" y="-99" width="28" height="30" rx="2" transform="rotate(240)"/>
      <rect x="-14" y="-99" width="28" height="30" rx="2" transform="rotate(270)"/>
      <rect x="-14" y="-99" width="28" height="30" rx="2" transform="rotate(300)"/>
      <rect x="-14" y="-99" width="28" height="30" rx="2" transform="rotate(330)"/>
    </g>

    <g id="gear">
      <use href="#gearTeeth" class="gear-gap"/>
      <use href="#gearTeeth" class="gear-face"/>
      <circle class="gear-hub" r="68"/>
    </g>

    <path id="arrowShape" d="M -143 -12 L -48 -12 L -48 -33 L 0 0 L -48 33 L -48 12 L -143 12 Z"/>
  </defs>

  <circle class="orbit-ring" cx="600" cy="463" r="337"/>

  <g class="flow-arrows">
    <use href="#arrowShape" class="flow-arrow" transform="translate(525 390) rotate(42.7)"/>
    <use href="#arrowShape" class="flow-arrow" transform="translate(675 389) rotate(137.3)"/>
    <use href="#arrowShape" class="flow-arrow" transform="translate(522 538) rotate(-42.7)"/>
    <use href="#arrowShape" class="flow-arrow" transform="translate(680 538) rotate(-137.3)"/>
  </g>

  <g class="gear-node rebalance" transform="translate(346 223)">
    <use href="#gear"/>
    <text class="gear-label" y="-16">Rebalance</text>
    <text class="gear-label" y="4">Annually</text>
    <text class="gear-note" y="23">LOREN IPSUM</text>
    <text class="gear-note" y="33">LOREN</text>
  </g>

  <g class="gear-node trend" transform="translate(853 223)">
    <use href="#gear"/>
    <text class="gear-label" y="-16">Trend</text>
    <text class="gear-label" y="4">33%</text>
    <text class="gear-label" y="24">Allocation</text>
  </g>

  <g class="gear-node buy-hold" transform="translate(346 704)">
    <use href="#gear"/>
    <text class="gear-label" y="-15">Buy &amp; Hold</text>
    <text class="gear-label" y="5">33%</text>
    <text class="gear-label" y="25">Allocation</text>
  </g>

  <g class="gear-node tactical" transform="translate(853 704)">
    <use href="#gear"/>
    <text class="gear-label" y="-15">Tactical</text>
    <text class="gear-label" y="5">33%</text>
    <text class="gear-label" y="25">Allocation</text>
  </g>

  <g class="gear-node strategy-core" transform="translate(600 463)">
    <use href="#gear"/>
    <text class="gear-label" y="-25">5Marble</text>
    <text class="gear-label" y="-5">World Stock</text>
    <text class="gear-label" y="15">Index</text>
    <text class="gear-label" y="35">Strategy</text>
  </g>
</svg>
</body>
</html>
```